Business Card Design

our business is purchasing, rehabbing and flipping homes. Design a house in the palm of a hand. This card is for a new company based in Georgia. So we buy homes that have been foreclosed, short sales,abandond, old homes and vacant homes.
We help improve the communities that we work in. We would like to see designs that use a black background with green accent and other colors that blend and don't take away from the logo and other important information.

Industry/Entity Type

Business

Contact Information for Business Card

Mavenbrook Holdings
Turning Old Doors Into New Starts
2738 Fenwick Ln
Orvale TX 75418
Office: 555-014-0192
mavenbrookholdingsllc.example

```html
<!DOCTYPE html>
<html lang="en">
<head>
<meta charset="utf-8">
<title>Mavenbrook Holdings – Business Card</title>
<link rel="stylesheet" href="https://fonts.googleapis.com/css2?family=Open+Sans:wght@400&display=swap">
<style>
  :root {
    --page: #ffffff;
    --card: #3a3a3a;
    --card-edge: #2e2e2e;
    --green: #00a859;
    --icon: #2b2b2b;
    --text: #ffffff;
  }
  html, body {
    margin: 0;
    padding: 0;
    width: 1200px;
    height: 705px;
    overflow: hidden;
    background: var(--page);
  }
  .card {
    position: relative;
    width: 1200px;
    height: 705px;
    box-sizing: border-box;
    border-radius: 34px;
    border: 2px solid var(--card-edge);
    background: var(--card);
    overflow: hidden;
    font-family: "Open Sans", sans-serif;
    color: var(--text);
  }
  .brand {
    position: absolute;
    left: 105px;
    top: 300px;
    width: 290px;
    display: flex;
    align-items: center;
    gap: 14px;
  }
  .brand-mark {
    flex: none;
    width: 22px;
    height: 22px;
    border-radius: 50%;
    background: var(--green);
  }
  .brand-name {
    font-size: 31px;
    font-weight: 400;
    line-height: 1.25;
    color: var(--text);
  }
  .icon-box {
    position: absolute;
    left: 525px;
    width: 86px;
    height: 88px;
    border-radius: 7px;
    background: var(--green);
    display: flex;
    align-items: center;
    justify-content: center;
  }
  .icon-box svg { display: block; }
  .rule {
    position: absolute;
    left: 605px;
    right: 0;
    height: 22px;
    background: var(--green);
  }
  .icon-box.location { top: 132px; }
  .rule.location { top: 167px; }
  .icon-box.phone { top: 327px; }
  .rule.phone { top: 360px; }
  .icon-box.email { top: 492px; }
  .rule.email { top: 527px; }
  .info {
    position: absolute;
    left: 628px;
    margin: 0;
    font-size: 31px;
    font-weight: 400;
    line-height: 1;
    white-space: nowrap;
  }
  .info.tagline-1 { top: 199px; }
  .info.tagline-2 { top: 256px; }
  .info.address { top: 314px; }
  .info.office { top: 416px; }
  .info.website { top: 562px; }
</style>
</head>
<body>
  <main class="card">
    <div class="brand">
      <span class="brand-mark"></span>
      <span class="brand-name">Mavenbrook<br>Holdings</span>
    </div>

    <div class="rule location"></div>
    <div class="icon-box location">
      <svg width="34" height="58" viewBox="0 0 34 58" aria-hidden="true">
        <path fill="var(--icon)" d="M17 0C7.6 0 0 7.6 0 17c0 10 9 16 17 41 8-25 17-31 17-41C34 7.6 26.4 0 17 0z"/>
        <circle cx="17" cy="16" r="6.5" fill="var(--green)"/>
      </svg>
    </div>

    <p class="info tagline-1">Mavenbrook Holdings Turning</p>
    <p class="info tagline-2">Old Doors Into New Starts</p>
    <p class="info address">2738 Fenwick Ln Orvale TX 75418</p>

    <div class="rule phone"></div>
    <div class="icon-box phone">
      <svg width="40" height="56" viewBox="0 0 40 56" aria-hidden="true">
        <path fill="var(--icon)" d="M14 2l8 12-6 5c2 8 6 15 12 21l6-4 6 11-7 6C20 54 6 38 4 16 4 9 8 4 14 2z"/>
      </svg>
    </div>
    <p class="info office">Office: 555-014-0192</p>

    <div class="rule email"></div>
    <div class="icon-box email">
      <svg width="58" height="40" viewBox="0 0 58 40" aria-hidden="true">
        <rect x="2" y="2" width="54" height="36" fill="none" stroke="var(--icon)" stroke-width="4"/>
        <path d="M2 2l27 22L56 2M2 38l20-18M56 38L36 20" fill="none" stroke="var(--icon)" stroke-width="4"/>
      </svg>
    </div>
    <p class="info website">mavenbrookholdingsllc.example</p>
  </main>
</body>
</html>
```